Upmarket Bathroom and Kitchen ware supplier needs a classy business card design

We are a company based in Fiji, we sell plumbing ware (Kitchen and bathroom taps, Basins,showers, toilets etc) through up market show rooms to individuals and directly through Architects and designers of resorts and holiday houses for new builds and renovations. we are wanting to upgrade our over all look and brand. we are starting with a new logo but will be rebranding the whole business. This project is for a business card design for my management and tales team I would like it to be dark, classy and interesting

Target Market(s)

Resort directors and Management, High end holiday home owners

Contact Information for Business Card

Neil Dawson
Director
+64219473815

Colors

Designer to choose colors to be used in the design.

Requirements
Must have
• Must have an upmarket appearance I like darker charcoal shades but will be guided by the designers
• Please any catch phrases like "Crafting remarkable living rooms" this belongs tpo one of our suppliers so can not be used.
Nice to have
• Double sided, so front dedicated to logo provided and back info about the business and the person.

```html
<!DOCTYPE html>
<html lang="en">
<head>
<meta charset="utf-8">
<title>Coralis Interiors – Business Card</title>
<link rel="stylesheet" href="https://fonts.googleapis.com/css2?family=Montserrat:wght@400;500;700&display=swap">
<style>
  :root {
    --backdrop: #6c7a80;
    --card: #ffffff;
    --charcoal: #323232;
    --slate: #656565;
    --ink: #111111;
    --paper-text: #ffffff;
    --icon-bg: #5e5e5e;
    --rule: #4a4a4a;
  }
  * { margin: 0; padding: 0; box-sizing: border-box; }
  html, body {
    width: 1200px; height: 1200px; overflow: hidden;
    background: var(--backdrop);
    font-family: "Montserrat", sans-serif;
  }
  .card {
    position: absolute; left: 252px;
    width: 696px; height: 414px;
    background: var(--card);
    overflow: hidden;
  }
  .card--front { top: 121px; }
  .card--back { top: 620px; }

  .front-shapes { position: absolute; inset: 0; }

  .brand {
    position: absolute;
    display: flex; align-items: center; gap: 14px;
    color: var(--ink);
  }
  .brand__dot {
    width: 14px; height: 14px; border-radius: 50%;
    background: currentColor; flex: none;
  }
  .brand__name {
    font-weight: 400; font-size: 21px; letter-spacing: 6px;
    line-height: 1.35; text-transform: uppercase;
  }
  .card--front .brand { left: 372px; top: 68px; }

  .person {
    position: absolute; left: 103px; top: 144px;
    color: var(--paper-text);
  }
  .person__name { font-weight: 700; font-size: 18px; letter-spacing: 0.2px; }
  .person__role { font-weight: 400; font-size: 15px; margin-top: 3px; }

  .contact {
    position: absolute; left: 102px;
    display: flex; align-items: center; gap: 20px;
    color: var(--paper-text); font-size: 14px;
  }
  .contact--phone { top: 206px; }
  .contact--email { top: 234px; }
  .contact__icon {
    width: 21px; height: 21px; border-radius: 50%;
    background: var(--icon-bg);
    display: flex; align-items: center; justify-content: center;
  }

  .divider {
    position: absolute; left: 324px; top: 169px;
    width: 1px; height: 83px; background: var(--rule);
  }

  .address {
    position: absolute; left: 383px; top: 195px;
    color: var(--paper-text); font-size: 14px; line-height: 19px;
  }

  .back-band {
    position: absolute; left: 22px; top: 153px;
    width: 653px; height: 112px;
    background: var(--charcoal);
  }
  .card--back .brand {
    color: var(--paper-text);
    left: 0; right: 0; top: 180px; justify-content: center;
  }
</style>
</head>
<body>

<section class="card card--front" aria-label="Business card front">
  <svg class="front-shapes" width="696" height="414" viewBox="0 0 696 414">
    <rect class="address-band" x="330" y="176" width="343" height="76" fill="var(--slate)"/>
    <polygon class="name-panel" points="21,20 286,20 410,393 21,393" fill="var(--charcoal)"/>
  </svg>

  <div class="brand">
    <span class="brand__dot"></span>
    <span class="brand__name">Coralis<br>Interiors</span>
  </div>

  <div class="person">
    <p class="person__name">NEIL DAWSON</p>
    <p class="person__role">Director</p>
  </div>

  <div class="contact contact--phone">
    <span class="contact__icon">
      <svg width="12" height="12" viewBox="0 0 24 24"><path fill="#fff" d="M6.6 10.8a15.1 15.1 0 0 0 6.6 6.6l2.2-2.2c.3-.3.7-.4 1-.2 1.1.4 2.3.6 3.6.6.6 0 1 .4 1 1V20c0 .6-.4 1-1 1A17 17 0 0 1 3 4c0-.6.4-1 1-1h3.5c.6 0 1 .4 1 1 0 1.3.2 2.5.6 3.6.1.3 0 .7-.2 1z"/></svg>
    </span>
    <span>+64219473815</span>
  </div>
  <div class="contact contact--email">
    <span class="contact__icon">
      <svg width="12" height="10" viewBox="0 0 24 18"><rect x="1" y="1" width="22" height="16" fill="none" stroke="#fff" stroke-width="2"/><path d="M1 1l11 9 11-9" fill="none" stroke="#fff" stroke-width="2"/></svg>
    </span>
    <span>hello@coralis.fj</span>
  </div>

  <span class="divider"></span>

  <p class="address">Your Location Address<br>Here</p>
</section>

<section class="card card--back" aria-label="Business card back">
  <div class="back-band"></div>
  <div class="brand">
    <span class="brand__dot"></span>
    <span class="brand__name">Coralis<br>Interiors</span>
  </div>
</section>

</body>
</html>
```